Business Card Design Project : Tidewell Press

In preparation for market launch, Whistler's Tidewell Press require the development of a business card. Tidewell Press is a Community online publishing web portal. We provide the the city of Whistler located in B.C. (Canada) business directories, News, Classified ads, News, Events and blogs etc.

The main focus of the brand is to help local businesses to corporate with their online advertisement and marketing. Meeting our clients face to face is a must (B2B).

Target Market(s)

The target market is B2B customers. Business Owners to Marketing, advertising Managers

Industry/Entity Type

Business

Requirements
Must have
• - The business card will be two sided.
the BACK side will have our logo which consist of (icon, url,slogan) submited. The logo will be middle and centred.

The FRONT side should have company details:

Company Legal Name: FERNDALE TIDEWELL PRESS

Owen Marsk
Director of Sales & Marketing

www.ferndaletidewell.biz
owen@ferndaletidewell.biz

Phone: 555 014 3826
#2817 - 562 E. Harlow Ave.
Vancouver, B.C. K7P2R4 Canada
Nice to have
• - For the "FRONT" side of our business card. You can separate or re-arrange with our logo components (icon, logo,slogan). It does not have to be together.

Also our company legal name is rather long so arrange or organize the name in a way to make it shorter. Your experience and creativity will have to come in play.
Should not have
• should not have other colors beside logo color and black text (2 colors). Also nothing Three dimensional

```html
<!DOCTYPE html>
<html lang="en">
<head>
<meta charset="utf-8">
<title>Tidewell Press — Business Card</title>
<link href="https://fonts.googleapis.com/css2?family=Open+Sans:wght@400;600;700&display=swap" rel="stylesheet">
<style>
  :root {
    --brand-blue: #1c6db3;
    --ink: #1d1b1c;
    --paper: #ffffff;
    --backdrop: #e7e7e5;
    --white: #ffffff;
  }
  * { box-sizing: border-box; margin: 0; padding: 0; }
  html, body { width: 1200px; height: 944px; overflow: hidden; }
  body {
    background: var(--backdrop);
    font-family: "Open Sans", Arial, sans-serif;
    color: var(--ink);
    position: relative;
  }
  .card {
    position: absolute;
    width: 580px;
    height: 330px;
    background: var(--paper);
    border-radius: 26px;
    overflow: hidden;
  }
  /* Back side */
  .card-back { left: 70px; top: 100px; }
  .card-back .brand {
    position: absolute;
    left: 0; right: 0; top: 96px;
    display: flex; justify-content: center; align-items: center; gap: 16px;
  }
  .brand-dot {
    width: 34px; height: 34px; border-radius: 50%;
    background: var(--brand-blue);
  }
  .brand-name {
    font-weight: 700; color: var(--brand-blue);
    font-size: 50px; letter-spacing: -0.5px;
  }
  .card-back .url {
    position: absolute; left: 0; right: 0; top: 190px;
    text-align: center; font-weight: 700; font-size: 36px;
    letter-spacing: -0.8px; color: var(--ink);
  }
  .card-back .slogan {
    position: absolute; left: 0; right: 0; top: 236px;
    text-align: center; font-size: 29px; color: var(--brand-blue);
  }
  /* Front side */
  .card-front { left: 550px; top: 500px; }
  .front-panel { position: absolute; inset: 0; }
  .card-front .brand {
    position: absolute; left: 44px; top: 46px;
    display: flex; align-items: center; gap: 10px;
  }
  .card-front .brand-dot { width: 22px; height: 22px; }
  .card-front .brand-name { font-size: 30px; }
  .card-front .slogan {
    position: absolute; left: 44px; top: 96px;
    font-size: 19px; color: var(--brand-blue);
  }
  .contact {
    position: absolute; left: 34px; top: 146px;
    font-size: 15px; line-height: 20px; list-style: none;
  }
  .contact li { display: flex; gap: 8px; align-items: flex-start; margin-bottom: 5px; }
  .contact svg { flex: none; margin-top: 3px; }
  .person {
    position: absolute; right: 26px; bottom: 44px;
    width: 230px;
    text-align: center; color: var(--white);
  }
  .person-name { font-size: 21px; font-weight: 400; line-height: 28px; }
  .person-role { font-size: 14px; line-height: 20px; }
</style>
</head>
<body>

<section class="card card-back" aria-label="Business card, back side">
  <div class="brand">
    <span class="brand-dot"></span>
    <span class="brand-name">Tidewell Press</span>
  </div>
  <p class="url">www.ferndaletidewell.biz</p>
  <p class="slogan">Your information gateway</p>
</section>

<section class="card card-front" aria-label="Business card, front side">
  <svg class="front-panel" width="580" height="330" viewBox="0 0 580 330" aria-hidden="true">
    <path d="M250 330 C330 262 398 130 420 0 L580 0 L580 330 Z" fill="var(--brand-blue)"/>
    <path d="M222 330 C304 260 372 130 392 0 L420 0 C398 130 330 262 250 330 Z" fill="var(--ink)"/>
  </svg>

  <div class="brand">
    <span class="brand-dot"></span>
    <span class="brand-name">Tidewell Press</span>
  </div>
  <p class="slogan">Your information gateway</p>

  <ul class="contact">
    <li>
      <svg width="14" height="13" viewBox="0 0 14 13"><path d="M7 0 L14 6 H12 V13 H8.5 V9 H5.5 V13 H2 V6 H0 Z" fill="var(--ink)"/></svg>
      <span>#2817 - 562 E. Harlow Ave.<br>Vancouver, B.C. K7P2R4 Canada</span>
    </li>
    <li>
      <svg width="14" height="14" viewBox="0 0 14 14"><circle cx="7" cy="7" r="6.5" fill="none" stroke="var(--brand-blue)" stroke-width="1.2"/><path d="M4.5 3.5 L6 3.5 L6.6 5.5 L5.6 6.3 C6.1 7.4 6.7 8 7.7 8.5 L8.5 7.5 L10.5 8.1 L10.5 9.6 C7 10 4 7 4.5 3.5 Z" fill="var(--brand-blue)"/></svg>
      <span>555 014 3826</span>
    </li>
    <li>
      <svg width="14" height="14" viewBox="0 0 14 14"><circle cx="7" cy="7" r="7" fill="var(--brand-blue)"/><rect x="3" y="4.5" width="8" height="5.5" fill="var(--white)"/><path d="M3 4.5 L7 7.5 L11 4.5" fill="none" stroke="var(--brand-blue)" stroke-width="0.9"/></svg>
      <span>owen@ferndaletidewell.biz</span>
    </li>
    <li>
      <svg width="14" height="14" viewBox="0 0 14 14"><circle cx="7" cy="7" r="7" fill="var(--brand-blue)"/></svg>
      <span>www.ferndaletidewell.biz</span>
    </li>
  </ul>

  <div class="person">
    <p class="person-name">Owen Marsk</p>
    <p class="person-role">Director of Sales &amp; Marketing</p>
  </div>
</section>

</body>
</html>
```